Business Card Design Project

New Private residential substance abuse treatment facility in Mapleton, UT. Facility located in elegant 11,000 home with stunning views of the mountains. Wish to incorporate colored logo. Business name- Cedar Brook Wellness. Facility is Tudor style with traditional furnishings, an overhead picture is attached. Lettering in a simple scroll or old english style. Must be easy to read with clear moderetly large font.
Updates

It seems the project time frame listed was not correct- it is a week.

Target Market(s)

Adults 18 and over with substance abuse issues requiring residential rehabilitation. Referral base are medical/mental health professionals, families and community agencies.

Industry/Entity Type

Residential

Colors
9bcb3b
fece3e
fbee3f

Requirements
Must have
• Clear and easy to read, professional and upscale presentation. Need logo, name, title, address, phone, fax and web page address. May add slogan later. Use same font as logo.
Nice to have
• Logo has a green mountain and a gold maple leaf so a nature themed element may work. Want to promote peaceful grounded image. Logo attached.
Should not have
• No tiny or complicated font. No modern or tech looking images. No light colored fonts.

```html
<!DOCTYPE html>
<html lang="en">
<head>
<meta charset="utf-8">
<title>Cedar Brook Wellness – Business Card</title>
<link rel="stylesheet" href="https://fonts.googleapis.com/css2?family=Alegreya:wght@400;500&display=swap">
<style>
  :root {
    --backdrop: #bcbdbf;
    --card: #ffffff;
    --ink: #1f1f1f;
    --brand-ink: #3f3f3f;
    --band-green: #8dc63f;
    --leaf-light: #f6ecc8;
    --leaf-mid: #efdca4;
    --shadow: rgba(0, 0, 0, 0.45);
  }
  * { margin: 0; padding: 0; box-sizing: border-box; }
  html, body {
    width: 1200px;
    height: 1200px;
    overflow: hidden;
    background: var(--backdrop);
    font-family: "Alegreya", Georgia, serif;
  }
  .stage {
    position: relative;
    width: 1200px;
    height: 1200px;
    display: flex;
    align-items: center;
    justify-content: center;
  }
  .business-card {
    position: relative;
    width: 840px;
    height: 466px;
    background: var(--card);
    box-shadow: 6px 6px 8px var(--shadow);
    overflow: hidden;
    color: var(--ink);
  }
  .leaf-art {
    position: absolute;
    top: 0;
    right: 0;
    width: 332px;
    height: 350px;
    background: radial-gradient(ellipse at 60% 45%, var(--leaf-mid) 0%, var(--leaf-light) 55%, rgba(246, 236, 200, 0) 78%);
  }
  .brand-name {
    position: absolute;
    left: 40px;
    top: 100px;
    display: flex;
    align-items: center;
    gap: 12px;
    font-size: 40px;
    font-weight: 500;
    color: var(--brand-ink);
    line-height: 1;
  }
  .brand-mark {
    width: 16px;
    height: 16px;
    border-radius: 50%;
    background: var(--band-green);
  }
  .person {
    position: absolute;
    left: 40px;
    top: 178px;
  }
  .person-name { font-size: 27px; font-weight: 400; line-height: 1.2; }
  .person-title { font-size: 24px; line-height: 1.3; }
  .contact {
    position: absolute;
    left: 40px;
    top: 270px;
    font-size: 24px;
    line-height: 40px;
  }
  .web-band {
    position: absolute;
    left: 0;
    bottom: 0;
    width: 100%;
    height: 50px;
    background: var(--band-green);
    display: flex;
    align-items: center;
    justify-content: center;
    font-size: 23px;
    letter-spacing: 4.2px;
    color: var(--ink);
  }
</style>
</head>
<body>
<main class="stage">
  <article class="business-card">
    <div class="leaf-art" role="img" aria-label="Large pale gold maple leaf illustration with fine veins"></div>

    <div class="brand-name"><span class="brand-mark"></span>Cedar Brook Wellness</div>

    <div class="person">
      <p class="person-name">FirstName SurName</p>
      <p class="person-title">TITLE</p>
    </div>

    <div class="contact">
      <p>Address Line 1, Address Line 2</p>
      <p>Address Line 3, Postcode</p>
      <p>P: (00) 123 4567,&nbsp; F: (00) 123 45567</p>
    </div>

    <footer class="web-band">www.cedarbrookwellness.com</footer>
  </article>
</main>
</body>
</html>
```